The Wisdom of Lanterns New Book Cover Design Project

Book cover design . Paperback, ebook, and Talvora (derived from book cover) files/images required.
Book Title: The Wisdom of Lanterns
Subtitle: Under Copper Bridges
Author: Daniel Forsythe
Files: Ebook, Paperback (Brindlewick & Halvern Quill), Talvora sized image
File size & information to be provided once design is ready. Brindlewick paperback will be 5.25 x 8.
Completion date is flexible. Planning to publish in November.
Updates

Target Market(s)

Motorcycle owners

Font styles to use
Sans Serif

Requirements
Must have
• A generic looking motorcycle (samples attached). Thumbnail easily recognized as a motorcycle book.
Nice to have
• Open to all ideas but am favoring my idea: to emphasize the title lettering similar to (but not a copy of) other Wisdom books (examples attached), on a plain background. All books in the category have a motorcycle on the cover. Author name and subtitle do not have to be prominent. Rider optional..
Should not have
• Should not look like a biker romance or fantasy cover or look cartoonish. Motorcycle pic should be fairly generic (brand, style,).

```html
<!DOCTYPE html>
<html lang="en">
<head>
<meta charset="utf-8">
<title>The Wisdom of Lanterns — Daniel Forsythe</title>
<link rel="stylesheet" href="https://fonts.googleapis.com/css2?family=Bodoni+Moda:wght@400;500;700&family=Playfair+Display:wght@400;700&display=swap">
<style>
  :root {
    --paper: #ffffff;
    --ink: #0a0a0a;
    --accent: #e8262b;
    --chrome-light: #e9e9e9;
    --chrome-dark: #1a1a1a;
  }
  * { margin: 0; padding: 0; box-sizing: border-box; }
  html, body {
    width: 840px;
    height: 1200px;
    overflow: hidden;
    background: var(--paper);
  }
  .cover {
    position: relative;
    width: 840px;
    height: 1200px;
    background: var(--paper);
    color: var(--ink);
  }
  .title-initial {
    position: absolute;
    left: 80px;
    top: 170px;
    width: 240px;
    height: 710px;
  }
  .title-initial text {
    font-family: "Playfair Display", "Bodoni Moda", serif;
    font-weight: 700;
    fill: var(--ink);
  }
  .title-subject {
    position: absolute;
    left: 322px;
    top: 288px;
    width: 60px;
    height: 586px;
    writing-mode: vertical-rl;
    font-family: "Bodoni Moda", "Playfair Display", serif;
    font-weight: 500;
    font-size: 74px;
    line-height: 60px;
    letter-spacing: 6px;
    color: var(--accent);
    white-space: nowrap;
  }
  .title-the,
  .title-of {
    position: absolute;
    font-family: "Bodoni Moda", serif;
    font-weight: 400;
    font-size: 36px;
    letter-spacing: 1px;
    color: var(--ink);
  }
  .title-the { left: 428px; top: 268px; }
  .title-of  { left: 452px; top: 480px; }
  .title-rest {
    position: absolute;
    left: 398px;
    top: 300px;
    font-family: "Playfair Display", "Bodoni Moda", serif;
    font-weight: 400;
    font-size: 118px;
    line-height: 1;
    letter-spacing: -2px;
    color: var(--ink);
  }
  .motorcycle {
    position: absolute;
    left: 400px;
    top: 625px;
    width: 300px;
    height: 250px;
    border-radius: 40px 60px 20px 20px;
    background: radial-gradient(ellipse at 55% 50%, #3a3a3a 0%, #1a1a1a 40%, #9a9a9a 70%, rgba(255,255,255,0) 100%);
  }
  .subtitle {
    position: absolute;
    left: 0;
    width: 840px;
    top: 1000px;
    text-align: center;
    font-family: "Bodoni Moda", serif;
    font-size: 28px;
    letter-spacing: 2px;
    color: var(--ink);
  }
  .author {
    position: absolute;
    left: 0;
    width: 840px;
    top: 1090px;
    text-align: center;
    font-family: "Bodoni Moda", serif;
    font-size: 38px;
    letter-spacing: 4px;
    color: var(--ink);
  }
</style>
</head>
<body>
  <main class="cover">
    <svg class="title-initial" viewBox="0 0 240 710" aria-hidden="true">
      <text x="120" y="705" text-anchor="middle" font-size="250" transform="scale(1,1)" textLength="236" lengthAdjust="spacingAndGlyphs" style="transform: scaleY(4); transform-origin: 120px 705px;">w</text>
    </svg>
    <h1 class="visually-title" style="position:absolute;left:-9999px;">The Wisdom of Lanterns</h1>
    <div class="title-subject" aria-hidden="true">LANTERNS</div>
    <div class="title-the" aria-hidden="true">THE</div>
    <div class="title-rest" aria-hidden="true">isdom</div>
    <div class="title-of" aria-hidden="true">OF</div>
    <div class="motorcycle" role="img" aria-label="Photograph of a black classic café-racer motorcycle with chrome exhaust and spoked wheels, seen from the side"></div>
    <p class="subtitle">Under Copper Bridges</p>
    <p class="author">DANIEL FORSYTHE</p>
  </main>
</body>
</html>
```